" Trata-se de uma clínica em início de funcionamento. Somos dois responsáveis técnicos (Psicólogos) e temos outros seis profissionais que estarão trabalhando conosco (também psicólogos). Temos uma médica Psiquiatra que fará parte da equipe. Ofereceremos atendimento nas abordagens: terapia cognitivo comportamental, humanista, psicanálise e Gestalt, entretanto, o foco será na Terapia Cognitivo-Comportamental (TCC). De forma breve, a base da TCC é: Nossos pensamentos, emoções e comportamentos estão interligados e influenciam um ao outro e são o foco principal do tratamento. Fazemos atendimentos individuais e em grupo. Além dos atendimentos de psicologia, a nossa proposta é oferecer outros serviços como palestras, cursos, treinamentos. Disponibilizamos de auditório para uso da clínica. No meu caso, tenho forte vínculo acadêmico. Sou pesquisadora do Núcleo de Estudos Clínicos da UNEVAR e faço mestrado em Saúde Mental na mesma instituição. Também pós-graduanda em TCC. Então o ensino será algo que terá um investimento forte, juntamente com os atendimentos clínicos. "

```html
<!DOCTYPE html>
<html lang="pt-BR">
<head>
<meta charset="UTF-8">
<title>Vertis Psicologia — Papel timbrado</title>
<link rel="stylesheet" href="https://fonts.googleapis.com/css2?family=Quicksand:wght@400;500;600&display=swap">
<style>
  :root {
    --backdrop: #e9e9ea;
    --paper: #ffffff;
    --teal: #5fb0a7;
    --teal-light: #7fc2b9;
    --navy: #13284a;
    --watermark: #f1f1f2;
    --footer-text: #ffffff;
  }
  * { margin: 0; padding: 0; box-sizing: border-box; }
  html, body {
    width: 1200px;
    height: 1200px;
    overflow: hidden;
    background: var(--backdrop);
    font-family: "Quicksand", sans-serif;
  }
  .letterhead {
    position: absolute;
    left: 211px;
    top: 50px;
    width: 778px;
    height: 1100px;
    background: var(--paper);
  }
  .brand {
    position: absolute;
    top: 48px;
    left: 0;
    width: 100%;
    display: flex;
    flex-direction: column;
    align-items: center;
  }
  .brand-name {
    display: flex;
    align-items: center;
    gap: 14px;
    color: var(--navy);
    font-weight: 500;
    font-size: 44px;
    letter-spacing: 1px;
    line-height: 1;
  }
  .brand-dot {
    width: 30px;
    height: 30px;
    border-radius: 50%;
    background: var(--teal-light);
  }
  .brand-tagline {
    margin-top: 6px;
    margin-left: 44px;
    color: var(--teal);
    font-weight: 500;
    font-size: 11px;
    letter-spacing: 7px;
    text-transform: uppercase;
  }
  .watermark {
    position: absolute;
    left: 73px;
    top: 311px;
    width: 633px;
    height: 480px;
    border-radius: 50%;
    background: radial-gradient(ellipse at center, var(--watermark) 0%, var(--watermark) 45%, rgba(241,241,242,0) 72%);
  }
  .footer-accent {
    position: absolute;
    left: 0;
    bottom: 70px;
    width: 100%;
    height: 11px;
    background: var(--teal);
  }
  .footer {
    position: absolute;
    left: 0;
    bottom: 0;
    width: 100%;
    height: 70px;
    background: var(--navy);
    display: flex;
    align-items: center;
    justify-content: center;
    gap: 8px;
    color: var(--footer-text);
    font-weight: 600;
    font-size: 14px;
  }
  .footer-icon { width: 14px; height: 18px; }
</style>
</head>
<body>
  <main class="letterhead">
    <header class="brand">
      <div class="brand-name"><span class="brand-dot"></span>VERTIS</div>
      <div class="brand-tagline">Psicologia</div>
    </header>

    <div class="watermark" role="img" aria-label="Marca d'água suave da clínica no centro da folha"></div>

    <div class="footer-accent"></div>
    <footer class="footer">
      <svg class="footer-icon" viewBox="0 0 14 18" aria-hidden="true">
        <path d="M7 1C3.7 1 1.2 3.5 1.2 6.7 1.2 11 7 17 7 17s5.8-6 5.8-10.3C12.8 3.5 10.3 1 7 1z" fill="none" stroke="#ffffff" stroke-width="1.6"/>
        <circle cx="7" cy="6.7" r="2" fill="none" stroke="#ffffff" stroke-width="1.4"/>
      </svg>
      <span class="footer-address">Endereço: Exemplo - N 11</span>
    </footer>
  </main>
</body>
</html>
```